redesing professional certificate

Redesign our certificate to more a professional look and to make it look like a-wanna have - Best in adobe photoshop, because this template will be our basic, and we have in our education different levels, basic, upper, lower, complex, master level. I usually add a small picture to show what level they are. Or when you have a better suggestion I a gladly to hear.
We teach to physiotherapist so it has to look professional.

Target Market(s)

physiotherapist

Industry/Entity Type

Health Care

Requirements
Must have
• our logo

```html
<!DOCTYPE html>
<html lang="en">
<head>
<meta charset="utf-8">
<title>Certificate of Achievement</title>
<link rel="stylesheet" href="https://fonts.googleapis.com/css2?family=Montserrat:wght@400;500;700;800&family=Pinyon+Script&family=Source+Sans+3:wght@400&display=swap">
<style>
  :root {
    --navy: #0d2540;
    --blue: #0a5b96;
    --blue-deep: #084a7c;
    --royal: #0b2f8f;
    --paper-light: #f4f4f5;
    --paper-mid: #d7d8da;
    --text: #1f3352;
    --ink: #111;
  }
  html, body { margin: 0; padding: 0; overflow: hidden; }
  body { width: 1200px; height: 927px; background: #fff; }
  .certificate {
    position: relative; width: 1200px; height: 927px; overflow: hidden;
    font-family: "Montserrat", sans-serif; color: var(--navy);
  }
  .backdrop, .artwork { position: absolute; inset: 0; }
  .brand {
    position: absolute; left: 987px; top: 36px; width: 174px; height: 174px;
    border-radius: 50%; background: var(--navy); border: 3px solid #fff;
    box-shadow: 0 0 0 2px var(--navy);
    display: flex; align-items: center; justify-content: center; text-align: center;
    color: #fff; font-weight: 700; font-size: 15px; line-height: 1.3; letter-spacing: 0.5px;
  }
  .title {
    position: absolute; left: 0; width: 1460px; top: 204px; margin: 0; text-align: center;
    font-weight: 800; font-size: 86px; letter-spacing: -1px; line-height: 1;
  }
  .subtitle {
    position: absolute; left: 0; width: 1460px; top: 294px; margin: 0; text-align: center;
    font-weight: 500; font-size: 30px; letter-spacing: 5px;
  }
  .ribbon { position: absolute; left: 439px; top: 339px; width: 583px; height: 58px; }
  .ribbon-text {
    position: absolute; left: 486px; top: 339px; width: 489px; height: 48px;
    display: flex; align-items: center; justify-content: center;
    color: #fff; font-size: 25px; font-weight: 500;
  }
  .recipient {
    position: absolute; left: 459px; width: 542px; top: 408px; margin: 0; text-align: center;
    font-family: "Pinyon Script", cursive; font-size: 86px; line-height: 1; color: var(--navy);
  }
  .recipient-line { position: absolute; left: 459px; top: 513px; width: 542px; height: 1px; background: var(--navy); }
  .course {
    position: absolute; left: 300px; width: 860px; top: 550px; margin: 0; text-align: center;
    font-size: 18px; line-height: 30px; color: var(--text);
  }
  .seal { position: absolute; left: 646px; top: 626px; width: 144px; height: 144px; }
  .seal-text {
    position: absolute; left: 646px; top: 626px; width: 144px; height: 144px;
    display: flex; flex-direction: column; align-items: center; justify-content: center;
    color: var(--royal); font-weight: 700; text-align: center;
  }
  .seal-label { font-size: 11px; line-height: 13px; }
  .seal-number { font-size: 19px; margin-top: 3px; }
  .signatory { position: absolute; width: 207px; text-align: center; }
  .signatory::before { content: ""; display: block; height: 1px; background: var(--ink); margin-bottom: 12px; }
  .signatory-name { font-weight: 700; font-size: 19px; color: var(--ink); }
  .signatory-role { font-size: 15px; color: var(--ink); margin-top: 1px; }
  .signatory-left { left: 368px; top: 699px; }
  .signatory-right { left: 876px; top: 699px; }
  .signatory-right .signatory-name { margin-top: 5px; }
  .disclaimer {
    position: absolute; left: 300px; width: 840px; top: 792px; margin: 0; text-align: center;
    font-family: "Source Sans 3", sans-serif; font-size: 18px; line-height: 22px; color: var(--ink);
  }
  .issuer {
    position: absolute; left: 420px; width: 600px; top: 848px; margin: 0; text-align: center;
    font-size: 12px; line-height: 14.5px; color: var(--ink); font-style: normal;
  }
</style>
</head>
<body>
<main class="certificate">
  <svg class="backdrop" width="1200" height="927" viewBox="0 0 1200 927" aria-hidden="true">
    <defs>
      <linearGradient id="paper" x1="0" y1="0" x2="1" y2="1">
        <stop offset="0" stop-color="#f6f6f7"/>
        <stop offset="0.5" stop-color="#e6e7e9"/>
        <stop offset="1" stop-color="#c9cacd"/>
      </linearGradient>
    </defs>
    <rect width="1200" height="927" fill="#0a5b96"/>
    <path d="M0 0 H560 C380 40 200 150 80 250 L0 230 Z" fill="#084a7c"/>
    <path d="M0 200 C150 260 300 250 420 180 C560 90 760 20 900 0 H1200 V0 Z" fill="#0b3358" opacity="0.55"/>
    <path d="M0 0 H1200 V10 C980 -10 720 10 560 60 C420 105 300 170 220 240 C160 230 60 200 0 180 Z" fill="#0a4f86" opacity="0.6"/>
    <circle cx="750" cy="660" r="648" fill="url(#paper)"/>
  </svg>

  <svg class="artwork" width="1200" height="927" viewBox="0 0 1200 927">
    <defs>
      <radialGradient id="glow-neck" cx="0.55" cy="0.6" r="0.7">
        <stop offset="0" stop-color="#3e5ee0"/><stop offset="1" stop-color="#06166a"/>
      </radialGradient>
      <radialGradient id="glow-knee" cx="0.45" cy="0.55" r="0.7">
        <stop offset="0" stop-color="#4f78ee"/><stop offset="1" stop-color="#0a2aa8"/>
      </radialGradient>
      <radialGradient id="glow-wrist" cx="0.45" cy="0.5" r="0.7">
        <stop offset="0" stop-color="#3c68ea"/><stop offset="1" stop-color="#0418a0"/>
      </radialGradient>
    </defs>
    <circle cx="312" cy="213" r="115" fill="url(#glow-neck)" role="img" aria-label="Illustration of a neck with highlighted cervical spine"/>
    <circle cx="158" cy="430" r="116" fill="url(#glow-knee)" role="img" aria-label="Illustration of a knee joint with highlighted pain area"/>
    <circle cx="131" cy="710" r="116" fill="url(#glow-wrist)" role="img" aria-label="Illustration of a hand and wrist with highlighted joint"/>
  </svg>

  <div class="brand">Connective<br>Motion<br>Therapy</div>

  <h1 class="title">CERTIFICATE</h1>
  <p class="subtitle">OF ACHIEVEMENT</p>

  <svg class="ribbon" viewBox="0 0 583 58" aria-hidden="true">
    <polygon points="0,20 60,20 60,58 0,58 30,39" fill="var(--navy)"/>
    <polygon points="583,20 523,20 523,58 583,58 553,39" fill="var(--navy)"/>
    <polygon points="47,48 88,48 88,58 47,58" fill="#061424"/>
    <polygon points="495,48 536,48 536,58 495,58" fill="#061424"/>
    <rect x="47" y="0" width="489" height="48" fill="var(--royal)"/>
  </svg>
  <div class="ribbon-text">This Certificate is Proudly Presented to</div>

  <h2 class="recipient">Marco Delgado</h2>
  <div class="recipient-line"></div>

  <p class="course">HAS COMPLETED THE MOTION THERAPY LEVEL I COURSE - 3 DAYS, 15 - 17 FEBRUARY 2020<br>KÓPAVOGUR, ICELAND 17 FEBRUARY 2020.</p>

  <svg class="seal" viewBox="0 0 144 144" aria-hidden="true">
    <defs>
      <linearGradient id="silver" x1="0" y1="0" x2="1" y2="1">
        <stop offset="0" stop-color="#f4f5f7"/><stop offset="0.5" stop-color="#c4c7cc"/><stop offset="1" stop-color="#eef0f2"/>
      </linearGradient>
    </defs>
    <circle cx="72" cy="72" r="68" fill="var(--royal)" stroke="var(--royal)" stroke-width="6" stroke-dasharray="4 3"/>
    <circle cx="72" cy="72" r="57" fill="url(#silver)"/>
  </svg>
  <div class="seal-text">
    <span class="seal-label">REGISTRATION<br>NUMBER</span>
    <span class="seal-number">1 ICE 20</span>
  </div>

  <div class="signatory signatory-left">
    <div class="signatory-name">Mr. JT van Lier</div>
    <div class="signatory-role">Co-Director</div>
  </div>
  <div class="signatory signatory-right">
    <div class="signatory-name">Mr. RK Solberg</div>
    <div class="signatory-role">Co-Director</div>
  </div>

  <p class="disclaimer">The Connective Motion Therapy ongoing certification is contingent upon meeting the requirements of the maintenance of the certification of Motion Therapy</p>

  <address class="issuer">MOTIONWEAVE BV<br>Lindengracht 48, 1015KJ Amsterdam, The Netherlands<br>Specialists in Motion Therapy Innovation</address>
</main>
</body>
</html>
```